Quality Improvement Software for healthcare agencies needs a website.

Veltrix820 is a software for hospices and home health agencies to manage their Quality Assurance Performance Improvement programs to remain complaint with the standards set by Sanovia and the Bureau of Civic Wellbeing. The web accessible software-as-a-service provides an easy, turn-key way for agencies to organize all the information they need to manage and track.

Coded - Design and coding required

4 page

```html
<!DOCTYPE html>
<html lang="en">
<head>
<meta charset="utf-8">
<title>Veltrix820 — Closing the Quality Improvement Loop</title>
<link href="https://fonts.googleapis.com/css2?family=Montserrat:wght@400;500;600;700&display=swap" rel="stylesheet">
<style>
:root{
  --blue:#1fa6f0;
  --orange:#f6921e;
  --green:#62b34a;
  --yellow:#f5c518;
  --ink:#1b1b1b;
  --muted:#555;
  --navy:#0c1a2c;
  --light:#bfe3fb;
  --white:#fff;
}
*{margin:0;padding:0;box-sizing:border-box}
html,body{width:1200px;height:3634px;overflow:hidden}
body{font-family:'Montserrat',sans-serif;color:var(--ink);background:var(--white);position:relative}
section,header,footer{position:absolute;left:0;width:1200px}
.abs{position:absolute}
.btn{position:absolute;display:inline-block;background:var(--blue);color:#fff;font-size:14px;font-weight:500;border-radius:20px;padding:10px 20px;text-decoration:none;white-space:nowrap}
.dots{display:flex;gap:3px;margin-top:6px}
.dots i{display:block;width:7px;height:5px}
.dots i:nth-child(1){background:var(--blue)}
.dots i:nth-child(2){background:var(--green)}
.dots i:nth-child(3){background:var(--orange)}
.dots i:nth-child(4){background:var(--yellow)}
.accent{color:var(--blue)}
.brand{display:flex;align-items:center;gap:8px;font-weight:600;font-size:30px;color:var(--ink)}
.brand-mark{width:22px;height:22px;background:var(--orange)}

/* corner ornaments */
.corner-ornament{position:absolute;width:97px;height:56px;z-index:2}
.corner-ornament.left{left:0;background:linear-gradient(90deg,rgba(31,166,240,.15),rgba(31,166,240,.55))}
.corner-ornament.right{left:1103px;background:linear-gradient(270deg,rgba(31,166,240,.15),rgba(31,166,240,.55))}

/* header */
.site-header{top:0;height:68px;background:#fff}
.site-header .brand{position:absolute;left:141px;top:16px}
.nav{position:absolute;left:487px;top:24px;display:flex;gap:27px;font-size:15px}
.nav a{color:var(--ink);text-decoration:none}
.nav a.active{color:var(--blue)}
.site-header .btn{left:939px;top:16px}

/* hero */
.hero{top:68px;height:565px;background:linear-gradient(100deg,#0f2238 0%,#163a5c 50%,#2c5f86 75%,#b88a6c 100%)}
.hero-title{position:absolute;left:141px;top:96px;font-size:58px;line-height:68px;font-weight:700;color:#fff}
.hero-title span{color:var(--orange);display:block}
.hero .btn{left:141px;top:402px}

/* about */
.about{top:633px;height:552px}
.about-photo{left:141px;top:85px;width:417px;height:353px;background:linear-gradient(135deg,#e9eef5,#c9d6e6 60%,#f2f4f8)}
.about-bars{left:455px;top:335px;width:133px;height:132px;background:linear-gradient(180deg,rgba(31,166,240,.15),rgba(31,166,240,.45))}
.about-brand{left:168px;top:360px;background:#fff;padding:8px 12px}
.about-text{left:641px;top:110px;width:420px}
.about-text h2{font-size:32px;font-weight:600}
.about-text .lead{font-size:13px;font-weight:500;line-height:21px;margin-top:20px}
.about-text .body{font-size:12.5px;color:var(--muted);line-height:21px;margin-top:14px}
.about .btn{left:641px;top:371px}

/* features */
.features{top:1185px;height:930px;background:radial-gradient(ellipse at 50% 40%,#4a4a4b,#2a2a2b 70%);color:#fff}
.features h2{position:absolute;top:72px;width:100%;text-align:center;font-size:32px;font-weight:600}
.features h2 + .dots{position:absolute;top:118px;left:587px}
.feature{position:absolute;width:200px;text-align:center}
.feature .ring{width:116px;height:116px;border-radius:50%;background:#fff;border:5px solid var(--blue);margin:0 auto;display:flex;align-items:center;justify-content:center}
.feature h3{font-size:16px;font-weight:600;margin-top:22px}
.feature p{font-size:12.5px;line-height:20.5px;margin:16px auto 0;width:186px}
.features .btn{left:536px;top:807px}

/* commitment */
.commit{top:2115px;height:525px;background:var(--light);overflow:hidden}
.commit-text{left:141px;top:112px;width:420px}
.commit-text h2{font-size:32px;font-weight:600}
.commit-text p{font-size:14px;line-height:23px;margin-top:22px}
.commit .btn{left:141px;top:375px}
.commit-photo{left:642px;top:87px;width:417px;height:354px;background:linear-gradient(120deg,#5d6166,#3d4a58 55%,#7fb6d4)}

/* testimonials */
.testimonials{top:2640px;height:535px}
.testimonials h2{position:absolute;top:80px;width:100%;text-align:center;font-size:32px;font-weight:600}
.testimonials h2 + .dots{position:absolute;top:126px;left:585px}
.card{position:absolute;top:160px;width:286px;height:290px;background:#fff;box-shadow:0 4px 18px rgba(0,0,0,.09);text-align:center;padding-top:28px}
.avatar{width:52px;height:52px;border-radius:50%;margin:0 auto;background:linear-gradient(180deg,#d9e6f2,#9bb4c9);border:2px solid var(--blue)}
.card h4{font-size:13px;font-weight:600;margin-top:14px}
.stars{color:var(--orange);font-size:13px;letter-spacing:2px;margin-top:6px}
.card p{font-size:12.5px;line-height:20.5px;padding:0 26px;margin-top:12px}
.arrow{position:absolute;top:289px;width:36px;height:36px;border-radius:50%}

/* footer */
.site-footer{top:3175px;height:459px;background:radial-gradient(ellipse at 60% 80%,#16324f,var(--navy) 70%);color:#fff}
.site-footer .brand{position:absolute;left:141px;top:98px;color:#fff}
.foot-about{left:143px;top:170px;width:230px;font-size:13px;line-height:21px}
.socials{left:141px;top:325px;display:flex;gap:14px}
.socials i{display:block;width:36px;height:36px;border-radius:50%;background:var(--blue)}
.foot-col h5{font-size:14px;font-weight:600}
.foot-col .dots{margin-bottom:18px}
.links a{display:block;color:#fff;text-decoration:none;font-size:13px;line-height:28px}
.links a.active{color:var(--blue)}
.contact-item{display:flex;align-items:center;gap:14px;font-size:13px;margin-bottom:20px;line-height:18px}
.contact-item svg{flex:none}
.foot-bar{left:141px;top:430px;width:918px;border-top:1px solid rgba(255,255,255,.35);padding-top:8px;display:flex;justify-content:space-between;font-size:12px}
</style>
</head>
<body>

<header class="site-header">
  <div class="brand"><span class="brand-mark"></span>Veltrix820</div>
  <nav class="nav">
    <a href="#" class="active">Home</a><a href="#">About Us</a><a href="#">Features</a><a href="#">Pricing</a><a href="#">Testimonials</a>
  </nav>
  <a class="btn" href="#">Contact Us</a>
</header>

<section class="hero" role="img" aria-label="Doctor in a white coat working on a tablet at a laptop, with a medical cross overlay">
  <h1 class="hero-title">Closing<br>The Quality<span>Improvement</span><span>Loop</span></h1>
  <a class="btn" href="#">Sign Up For A Free Trial</a>
</section>

<section class="about">
  <div class="abs about-photo" role="img" aria-label="Doctor's hands framing a floating health data dashboard"></div>
  <div class="abs about-bars"></div>
  <div class="abs about-brand"><div class="brand" style="font-size:28px"><span class="brand-mark"></span>Veltrix820</div></div>
  <div class="abs about-text">
    <h2>About <span class="accent">Veltrix820</span></h2>
    <div class="dots"><i></i><i></i><i></i><i></i></div>
    <p class="lead">Our web-accessible software-as-a-service is designed to simplify the process of remaining compliant with Sanovia and Bureau of Civic Wellbeing standards.</p>
    <p class="body">At Veltrix820, we understand the importance of organizing all the necessary information in one place. That's why our software provides an easy and turn-key way for hospices and home health agencies to manage and track their QAPI programs.</p>
  </div>
  <a class="btn" href="#">Read More</a>
</section>

<section class="features">
  <h2>Our Software <span class="accent">Features</span></h2>
  <div class="dots"><i></i><i></i><i></i><i></i></div>

  <div class="feature" style="left:136px;top:165px">
    <div class="ring"><svg width="48" height="48" viewBox="0 0 48 48" fill="none" stroke="#1b2a3a" stroke-width="3"><rect x="4" y="4" width="16" height="16" rx="4"/><rect x="28" y="4" width="16" height="16" rx="4"/><rect x="4" y="28" width="16" height="16" rx="4"/><rect x="28" y="28" width="16" height="16" rx="4"/></svg></div>
    <h3>Dashboard</h3>
    <p>Displays an overview of the user's QAPI program, including upcoming surveys, recent reports, and staff training status</p>
  </div>
  <div class="feature" style="left:378px;top:165px">
    <div class="ring"><svg width="46" height="46" viewBox="0 0 46 46" fill="none" stroke="#1b2a3a" stroke-width="2.5"><rect x="6" y="3" width="34" height="40"/><rect x="11" y="10" width="8" height="8"/><rect x="11" y="24" width="8" height="8"/><path d="M23 12h12M23 16h8M23 26h12M23 30h8"/></svg></div>
    <h3>Surveys</h3>
    <p>Lists all active surveys and allows users to create new ones using predefined templates or custom forms</p>
  </div>
  <div class="feature" style="left:620px;top:165px">
    <div class="ring"><svg width="44" height="46" viewBox="0 0 44 46" fill="none" stroke="#1b2a3a" stroke-width="2.5"><path d="M8 3h20l10 10v30H8z"/><path d="M28 3v10h10"/><path d="M13 32l7-8 5 5 8-9"/></svg></div>
    <h3>Reports</h3>
    <p>Displays a list of all closed surveys and their associated reports, with options to view or download them in various formats (PDF, Excel, CSV)</p>
  </div>
  <div class="feature" style="left:862px;top:165px">
    <div class="ring"><svg width="48" height="46" viewBox="0 0 48 46" fill="none" stroke="#1b2a3a" stroke-width="2.5"><rect x="14" y="4" width="26" height="16"/><circle cx="10" cy="18" r="4"/><circle cx="38" cy="28" r="4"/><path d="M4 42V28h12M44 42V36H30M12 30h26M18 30v12M30 30v12"/></svg></div>
    <h3>Meetings</h3>
    <p>Lists all scheduled meetings and allows users to add new ones or view past ones with notes and action items</p>
  </div>
  <div class="feature" style="left:258px;top:477px">
    <div class="ring"><svg width="48" height="46" viewBox="0 0 48 46" fill="none" stroke="#1b2a3a" stroke-width="2.5"><circle cx="24" cy="7" r="4"/><path d="M14 20h20v8H14z"/><circle cx="12" cy="32" r="3"/><circle cx="24" cy="32" r="3"/><circle cx="36" cy="32" r="3"/><path d="M4 42h40M24 11v9"/></svg></div>
    <h3>Staff Training</h3>
    <p>Tracks individual staff members' training progress and requirements based on their roles and responsibilities</p>
  </div>
  <div class="feature" style="left:500px;top:477px">
    <div class="ring"><svg width="44" height="46" viewBox="0 0 44 46" fill="none" stroke="#1b2a3a" stroke-width="2.5"><rect x="6" y="3" width="32" height="40"/><circle cx="21" cy="21" r="8"/><path d="M27 27l7 7"/></svg></div>
    <h3>Data Analysis</h3>
    <p>Provides tools for analyzing survey data using charts, graphs, and statistical tests to identify trends and areas for improvement</p>
  </div>
  <div class="feature" style="left:742px;top:477px">
    <div class="ring"><svg width="44" height="44" viewBox="0 0 44 44" fill="none" stroke="#1b2a3a" stroke-width="2.5"><circle cx="22" cy="22" r="7"/><path d="M22 3v7M22 34v7M3 22h7M34 22h7M8.6 8.6l5 5M30.4 30.4l5 5M8.6 35.4l5-5M30.4 13.6l5-5"/><circle cx="22" cy="22" r="13"/></svg></div>
    <h3>Settings</h3>
    <p>Allows users to customize their profile, preferences, and notifications; manage user accounts; and configure system settings like email templates and report formats</p>
  </div>
  <a class="btn" href="#">Read More</a>
</section>

<div class="corner-ornament left" style="top:2087px" role="img" aria-label="Blue zigzag line corner ornament"></div>

<section class="commit">
  <div class="abs commit-text">
    <h2>At <span class="accent">Veltrix820</span></h2>
    <div class="dots"><i></i><i></i><i></i><i></i></div>
    <p>At Veltrix820, we are committed to providing our clients with the best possible software solution for managing their <b>QAPI</b> programs. Our software is designed to be intuitive, user-friendly, and customizable to meet the unique needs of each agency. If you have any questions or would like to learn more about our software, please don't hesitate to contact us today!</p>
  </div>
  <a class="btn" href="#">Sign Up For A Free Trial</a>
  <div class="abs commit-photo" role="img" aria-label="Care team with a doctor and nurses reviewing a tablet in a hospital corridor"></div>
</section>

<div class="corner-ornament right" style="top:2610px" role="img" aria-label="Blue zigzag line corner ornament"></div>

<section class="testimonials">
  <h2>Our Satisfied <span class="accent">Customers</span></h2>
  <div class="dots"><i></i><i></i><i></i><i></i></div>
  <svg class="arrow" style="left:77px" viewBox="0 0 36 36"><circle cx="18" cy="18" r="17" fill="#fff" stroke="#1b1b1b" stroke-width="1.5"/><path d="M26 18H10M15 13l-5 5 5 5" stroke="#1b1b1b" stroke-width="1.5" fill="none"/></svg>
  <div class="card" style="left:141px"><div class="avatar" role="img" aria-label="Customer portrait"></div><h4>Tomas Reyl</h4><div class="stars">★★★★★</div><p>Standard dummy text ever since the 1500s, when an unknown printer took a galley of type and scrambled it to make a type specimen book. It has survived not only five centuries.</p></div>
  <div class="card" style="left:457px"><div class="avatar" role="img" aria-label="Customer portrait"></div><h4>Ilsa Morvane</h4><div class="stars">★★★★★</div><p>Standard dummy text ever since the 1500s, when an unknown printer took a galley of type and scrambled it to make a type specimen book. It has survived not only five centuries.</p></div>
  <div class="card" style="left:773px"><div class="avatar" role="img" aria-label="Customer portrait"></div><h4>Dena Quillo</h4><div class="stars">★★★★★</div><p>Standard dummy text ever since the 1500s, when an unknown printer took a galley of type and scrambled it to make a type specimen book. It has survived not only five centuries.</p></div>
  <svg class="arrow" style="left:1087px" viewBox="0 0 36 36"><circle cx="18" cy="18" r="18" fill="var(--blue)"/><path d="M10 18h16M21 13l5 5-5 5" stroke="#fff" stroke-width="1.5" fill="none"/></svg>
</section>

<div class="corner-ornament left" style="top:3145px" role="img" aria-label="Blue zigzag line corner ornament"></div>

<footer class="site-footer">
  <div class="brand"><span class="brand-mark"></span>Veltrix820</div>
  <p class="abs foot-about">Lorem ipsum dolor sit amet, consectetur adipiscing elit, sed do eiusmod tempor incididunt ut labore et dolore magna aliqua. Ut enim ad minim veniam.</p>
  <div class="abs socials"><i aria-label="Social link"></i><i aria-label="Social link"></i><i aria-label="Social link"></i><i aria-label="Social link"></i></div>
  <div class="abs foot-col" style="left:571px;top:100px">
    <h5>Quick Links</h5><div class="dots"><i></i><i></i><i></i><i></i></div>
    <div class="links"><a class="active" href="#">Home</a><a href="#">About Us</a><a href="#">Features</a><a href="#">Pricing</a><a href="#">Testimonials</a><a href="#">Contact Us</a></div>
  </div>
  <div class="abs foot-col" style="left:888px;top:100px">
    <h5>Contact Us</h5><div class="dots"><i></i><i></i><i></i><i></i></div>
    <div class="contact-item"><svg width="36" height="36" viewBox="0 0 36 36"><circle cx="18" cy="18" r="18" fill="var(--blue)"/><path d="M18 27s-6-6-6-10a6 6 0 0 1 12 0c0 4-6 10-6 10z" fill="#fff"/><circle cx="18" cy="17" r="2" fill="var(--blue)"/></svg><span>123, Lorem ipsum<br>dolor sit amet,</span></div>
    <div class="contact-item"><svg width="36" height="36" viewBox="0 0 36 36"><circle cx="18" cy="18" r="18" fill="var(--blue)"/><path d="M12 11l4 0 1 4-2 2a10 10 0 0 0 4 4l2-2 4 1v4c-8 0-13-5-13-13z" fill="#fff"/></svg><b>123 456 7890</b></div>
    <div class="contact-item"><svg width="36" height="36" viewBox="0 0 36 36"><circle cx="18" cy="18" r="18" fill="var(--blue)"/><rect x="10" y="12" width="16" height="12" fill="#fff"/><path d="M10 12l8 7 8-7" stroke="var(--blue)" stroke-width="1.5" fill="none"/></svg><span>hello@veltrix820.io</span></div>
  </div>
  <div class="abs foot-bar"><span>Copyright © 2023 <b>Veltrix820</b>. All Rights Reserved.</span><span>Privacy Policy | Terms &amp; Conditions</span></div>
</footer>

</body>
</html>
```